Academic and Business book cover

I need a book cover for my academic and business book.
The focus is in international / global negotiation and influence (how to negotiate across cultures).
The book will be published on Brevora, both in Lumaro and printed edition. therefore I need something that works under Brevora guidelines.The final design should be elegant and still be able to stand out against the competition.
I would like to have orange+grey for the text colors on the cover, even if different options are welcome.
Title and my name are in the attached word doc.

Target Market(s)

graduates, Phds, from international business schools. Managers

Industry/Entity Type

Business

Font styles to use
Serif
Sans Serif

Colors

Requirements
Must have
• The title and my name should have elegant fonts.
Nice to have
• pictures of the world that don't have the "usual" Europe in the centre.

```html
<!DOCTYPE html>
<html lang="en">
<head>
<meta charset="utf-8">
<title>The 3Rs Blueprint — Book Cover</title>
<link href="https://fonts.googleapis.com/css2?family=Roboto+Condensed:wght@700&family=Arimo:wght@400;700&display=swap" rel="stylesheet">
<style>
  :root {
    --page-bg: #ffffff;
    --cover-navy: #0a1622;
    --cover-deep: #050a12;
    --accent-sky: #6cc3e6;
    --title-orange: #c8412b;
    --subtitle-white: #f4f6f8;
    --globe-glow: #5aa6d6;
    --globe-core: #1d5680;
  }
  * { margin: 0; padding: 0; box-sizing: border-box; }
  html, body {
    width: 1200px;
    height: 900px;
    overflow: hidden;
    background: var(--page-bg);
  }
  .cover {
    position: absolute;
    left: 283px;
    top: 0;
    width: 635px;
    height: 900px;
    overflow: hidden;
    background: linear-gradient(180deg, var(--cover-navy) 0%, #0b1a28 40%, var(--cover-deep) 60%, #03070d 100%);
  }
  .spine-accent {
    position: absolute;
    left: 0;
    top: 0;
    width: 17px;
    height: 395px;
    background: var(--accent-sky);
  }
  .globe-art {
    position: absolute;
    left: 0;
    top: 395px;
    width: 635px;
    height: 505px;
    background:
      radial-gradient(ellipse 62% 62% at 55% 100%, var(--globe-glow) 0%, var(--globe-core) 55%, rgba(20,60,95,0.55) 75%, rgba(3,7,13,0) 100%),
      radial-gradient(ellipse 95% 45% at 50% 45%, rgba(70,150,210,0.22) 0%, rgba(3,7,13,0) 70%);
  }
  .title {
    position: absolute;
    left: 80px;
    top: 104px;
    font-family: "Roboto Condensed", "Arial Narrow", sans-serif;
    font-weight: 700;
    font-size: 68px;
    line-height: 76px;
    letter-spacing: 2px;
    color: var(--title-orange);
    text-transform: uppercase;
  }
  .subtitle {
    position: absolute;
    left: 80px;
    top: 279px;
    font-family: "Arimo", Arial, sans-serif;
    font-weight: 400;
    font-size: 32px;
    line-height: 43px;
    color: var(--subtitle-white);
    text-transform: uppercase;
  }
  .author {
    position: absolute;
    left: 80px;
    top: 790px;
    font-family: "Arimo", Arial, sans-serif;
    font-weight: 700;
    font-size: 37px;
    letter-spacing: 1.5px;
    color: var(--title-orange);
    text-transform: uppercase;
  }
</style>
</head>
<body>
  <main class="cover">
    <div class="spine-accent"></div>
    <div class="globe-art" role="img" aria-label="Glowing blue globe seen from above, wrapped in arcs of light connecting points around the world against a starry dark sky"></div>
    <h1 class="title">The 3Rs<br>Blueprint</h1>
    <p class="subtitle">Strategic persuasion and<br>dialogue principles for<br>cross-border leadership</p>
    <p class="author">Helena M. Corvetti</p>
  </main>
</body>
</html>
```